Website Landing Page for Medical Recruitment

Looking for a landing page to add to our existing website. The objective of the page is to recruit new clinical staff for various departments within PineHollow Medical Center (non-profit hospital in the Richmond, TX area).

We would like the page to be modern, professional, and non-cluttered. Please include call-to-actions and include a button that will navigate to the page where candidates can submit their applications (this page already exists).

Target Market(s)

25-35-year-olds who live in the Houston and Richmond area with medical experience.

Industry/Entity Type

Medical/Health

Font styles to use
Sans Serif

Colors
0054AA
0677BA
7BADD7
CADEEF
E8F1F8

Requirements
Must have
• A "call to action"; a button that navigates to pinehollowmedcenter.example/careers

```html
<!DOCTYPE html>
<html lang="en">
<head>
<meta charset="utf-8">
<title>PineHollow Medical Center – Careers</title>
<link href="https://fonts.googleapis.com/css2?family=Barlow+Semi+Condensed:wght@500;600;700&family=Roboto:wght@400;500&family=Poppins:wght@400;600&display=swap" rel="stylesheet">
<style>
:root{
  --navy:#2d5a94;
  --deep:#0f3a78;
  --sky:#7badd7;
  --mist:#cadeef;
  --ice:#e8f1f8;
  --ink:#1a1a1a;
  --white:#ffffff;
  --grey:#e6e6e6;
  --head:'Barlow Semi Condensed',sans-serif;
}
*{box-sizing:border-box;margin:0;padding:0}
html,body{width:1200px;height:2217px;overflow:hidden}
body{position:relative;background:var(--white);font-family:'Roboto',sans-serif;color:var(--ink)}
a{color:inherit;text-decoration:none}
.abs{position:absolute}

/* hero */
.hero-bg{left:0;top:0;width:1200px;height:800px;background:linear-gradient(180deg,#f6eeee 0%,#efe9ee 22%,#dde0e8 45%,#c4cfdc 62%,#aebfb8 80%,#9fb09a 100%)}
.hero-ring{left:628px;top:208px;width:500px;height:500px;border-radius:50%;background:var(--navy)}
.hero-people{left:690px;top:195px;width:510px;height:590px;border-radius:240px 0 0 0;background:linear-gradient(160deg,rgba(250,246,244,.85) 0%,rgba(232,222,216,.9) 35%,rgba(240,242,246,.95) 65%,rgba(226,232,240,.95) 100%)}
.topbar{left:412px;top:0;width:788px;height:50px;background:var(--navy);clip-path:polygon(0 0,100% 0,100% 100%,35px 100%)}
.topbar span{position:absolute;top:14px;color:var(--white);font-size:16px}
.topbar .ic{position:absolute;top:6px;width:38px;height:38px;border-radius:50%;background:var(--white)}
.brand{left:98px;top:42px;display:flex;align-items:center;gap:10px;font-family:var(--head);font-weight:600;font-size:26px;color:var(--navy);white-space:nowrap}
.brand .dot{width:50px;height:50px;border-radius:50%;background:var(--navy)}
.nav{left:453px;top:78px;display:flex;gap:26px;font-family:'Roboto',sans-serif;font-size:17px;color:#333}
.hero-title{left:96px;top:284px;font-family:var(--head);font-weight:700;font-size:62px;line-height:70px;color:var(--ink)}
.hero-text{left:97px;top:431px;font-size:17px;line-height:26px;width:340px}
.cta{left:94px;top:504px;width:229px;height:55px;border-radius:28px;background:var(--navy);display:flex;align-items:center;padding-left:10px;gap:20px;color:var(--white);font-family:var(--head);font-weight:600;font-size:24px;box-shadow:0 4px 8px rgba(0,0,0,.2)}
.cta i{width:36px;height:36px;border-radius:50%;background:var(--white)}
.round-btn{width:60px;height:60px;border-radius:50%;background:var(--white);box-shadow:0 2px 8px rgba(0,0,0,.18);display:flex;align-items:center;justify-content:center}

/* staff */
.section-title{left:0;width:1200px;top:848px;text-align:center;font-family:var(--head);font-weight:600;font-size:33px;color:var(--navy)}
.role{width:312px;height:326px;border-radius:50%;border:4px solid var(--navy);overflow:hidden;background:var(--white)}
.role .photo{position:absolute;left:0;right:0;top:0;height:235px}
.role h3{position:absolute;left:0;right:0;text-align:center;font-family:var(--head);font-weight:600;font-size:23px;line-height:30px;color:var(--navy)}
.photo.care{background:linear-gradient(135deg,#e9edf0 0%,#c7d6e4 40%,#9fb9d4 60%,#eef0f2 100%);-webkit-mask:linear-gradient(180deg,#000 70%,transparent)}
.photo.desk{background:linear-gradient(135deg,#f3f4f4 0%,#e6dccd 45%,#d9c4a9 70%,#f4efe8 100%);-webkit-mask:linear-gradient(180deg,#000 70%,transparent)}
.photo.phone{background:linear-gradient(135deg,#e7ebee 0%,#b5d2db 45%,#6aa7bd 60%,#eef0f2 100%);-webkit-mask:linear-gradient(180deg,#000 70%,transparent)}
.photo.forms{background:linear-gradient(135deg,#b9cfe6 0%,#7fa6cc 35%,#d7ccc2 65%,#f2f2f2 100%);-webkit-mask:linear-gradient(180deg,#000 70%,transparent)}
.role.active .photo{height:100%;background:linear-gradient(180deg,#8cc2d6 0%,#5e97b7 40%,#4277a8 70%,#3a67a0 100%)}
.role.active h3{color:var(--white)}
.apply{position:absolute;left:92px;top:239px;width:128px;height:48px;border-radius:24px;background:var(--white);border:2px solid var(--ink);font-family:var(--head);font-weight:500;font-size:19px;color:var(--navy);display:flex;align-items:center;justify-content:center}

/* footer */
.footer-bg{left:0;top:1700px;width:1200px;height:517px;background:var(--navy)}
.foot-h{font-family:'Poppins',sans-serif;font-weight:600;font-size:19px;color:var(--white)}
.links{list-style:none;font-family:'Poppins',sans-serif;font-size:16px;color:var(--white)}
.links li{position:relative;padding-left:22px}
.links li::before{content:"›";position:absolute;left:0;top:-1px}
.contact{font-family:'Poppins',sans-serif;font-size:16px;color:var(--white);line-height:26px}
.social{width:40px;height:40px;border-radius:50%;border:2px solid var(--white)}
.card{width:55px;height:38px;border-radius:4px;box-shadow:0 3px 0 rgba(0,0,0,.15)}
.rule{left:97px;top:2129px;width:1004px;height:1px;background:rgba(255,255,255,.7)}
.copy{left:0;width:1200px;top:2161px;text-align:center;font-family:'Poppins',sans-serif;font-size:18px;color:var(--white)}
</style>
</head>
<body>

<div class="abs hero-bg" role="img" aria-label="Soft faded photo of the hospital campus at dusk"></div>
<div class="abs hero-ring"></div>
<div class="abs hero-people" role="img" aria-label="Two smiling doctors in white coats giving a thumbs up"></div>

<div class="abs topbar">
  <div class="ic" style="left:56px"></div>
  <span style="left:118px">+1 281-555-0142</span>
  <div class="ic" style="left:286px"></div>
  <span style="left:347px">2240 Willow Lane, Richmond, Texas</span>
</div>
<svg class="abs" style="left:478px;top:16px" width="20" height="20" viewBox="0 0 24 24"><path fill="#2d5a94" d="M6.6 10.8a15 15 0 0 0 6.6 6.6l2.2-2.2a1 1 0 0 1 1-.2 11 11 0 0 0 3.6.6 1 1 0 0 1 1 1V20a1 1 0 0 1-1 1A17 17 0 0 1 3 4a1 1 0 0 1 1-1h3.5a1 1 0 0 1 1 1c0 1.2.2 2.4.6 3.6a1 1 0 0 1-.3 1z"/></svg>
<svg class="abs" style="left:707px;top:17px" width="22" height="18" viewBox="0 0 22 18"><rect width="22" height="18" rx="2" fill="#2d5a94"/><path d="M2 3l9 7 9-7" stroke="#fff" stroke-width="2" fill="none"/></svg>

<a class="abs brand" href="#"><span class="dot"></span>PineHollow Medical Center</a>

<nav class="abs nav"><a>Home</a><a>Find A Doctor</a><a>COVID-19</a><a>About Us</a><a>Services</a><a>Contact Us</a><a>More</a></nav>

<h1 class="abs hero-title">COVID-19 MOBILE<br>VACCINES</h1>
<p class="abs hero-text">See what patients have to say about us, and hear Daniela's story.</p>
<a class="abs cta" href="https://pinehollowmedcenter.example/careers"><i></i>JOB VACANCY</a>

<svg class="abs" style="left:0;top:680px" width="1200" height="140" viewBox="0 0 1200 140">
  <path d="M0 140 L0 60 C200 0 420 20 600 70 C800 120 1000 120 1200 70 L1200 140Z" fill="#e6e6e6"/>
  <path d="M0 140 L0 110 C200 30 420 40 600 90 C800 140 1000 130 1200 80 L1200 140Z" fill="#fff"/>
  <path d="M20 45 C200 5 420 15 600 65 C780 115 980 125 1200 70" stroke="#0f3a78" stroke-width="7" fill="none"/>
</svg>
<div class="abs round-btn" style="left:570px;top:727px"><svg width="14" height="9" viewBox="0 0 14 9"><path d="M1 1l6 6 6-6" stroke="#222" stroke-width="2" fill="none"/></svg></div>

<h2 class="abs section-title">HIRE CLINICAL STAFF</h2>

<div class="abs role" style="left:73px;top:924px">
  <div class="photo care" role="img" aria-label="Nurse assistant caring for an elderly patient"></div>
  <h3 style="top:236px">CERTIFIED NURSES<br>ASSISTANTS</h3>
</div>
<div class="abs role active" style="left:444px;top:924px">
  <div class="photo" role="img" aria-label="Emergency room staff working in an operating theatre"></div>
  <h3 style="top:167px">EMERGENCY ROOM<br>TECHS</h3>
  <a class="apply" href="https://pinehollowmedcenter.example/careers">Apply</a>
</div>
<div class="abs role" style="left:806px;top:924px">
  <div class="photo desk" role="img" aria-label="Two vocational nurses reviewing documents at a desk"></div>
  <h3 style="top:229px">LICENSED VOCATIONAL<br>NURSES</h3>
</div>
<div class="abs role" style="left:267px;top:1272px">
  <div class="photo phone" role="img" aria-label="Registered nurse on a phone call at a laptop"></div>
  <h3 style="top:234px">REGISTERED NURSES</h3>
</div>
<div class="abs role" style="left:611px;top:1272px">
  <div class="photo forms" role="img" aria-label="Unit secretary helping a patient fill in a form"></div>
  <h3 style="top:234px">UNIT SECRETARIES,<br>AND MORE</h3>
</div>

<div class="abs footer-bg"></div>
<svg class="abs" style="left:0;top:1620px" width="1200" height="120" viewBox="0 0 1200 120">
  <path d="M0 0 L1200 0 L1200 105 C1000 125 800 110 600 60 C420 15 200 10 0 65Z" fill="#fff"/>
  <path d="M0 65 C200 10 420 15 600 60 C800 110 1000 120 1200 90 L1200 105 C1000 125 800 115 600 75 C420 30 200 35 0 75Z" fill="#e6e6e6"/>
  <path d="M0 62 C200 5 420 10 600 55 C800 105 1000 125 1200 102" stroke="#0f3a78" stroke-width="7" fill="none"/>
</svg>
<div class="abs round-btn" style="left:571px;top:1652px"><svg width="14" height="9" viewBox="0 0 14 9"><path d="M1 8l6-6 6 6" stroke="#222" stroke-width="2" fill="none"/></svg></div>

<h4 class="abs foot-h" style="left:100px;top:1816px">QUICK LINKS</h4>
<ul class="abs links" style="left:100px;top:1878px;line-height:33.5px">
  <li>Home</li><li>Find A Doctor</li><li>COVID-19</li><li>About Us</li><li>Services</li><li>Contact Us</li><li>More</li>
</ul>

<h4 class="abs foot-h" style="left:300px;top:1818px">HELP LINKS</h4>
<ul class="abs links" style="left:300px;top:1880px;line-height:26px">
  <li>Terms &amp; Conditions</li><li>Privacy Policy</li><li>About Us</li><li>Support</li>
</ul>
<h4 class="abs foot-h" style="left:300px;top:2000px;font-weight:400">SOCIAL MEDIA</h4>
<span class="abs social" style="left:301px;top:2049px" aria-label="Social profile 1"></span>
<span class="abs social" style="left:364px;top:2049px" aria-label="Social profile 2"></span>
<span class="abs social" style="left:427px;top:2049px" aria-label="Social profile 3"></span>

<h4 class="abs foot-h" style="left:524px;top:1816px">CONTACT</h4>
<svg class="abs" style="left:527px;top:1862px" width="12" height="17" viewBox="0 0 12 17"><path d="M6 0a6 6 0 0 0-6 6c0 4.5 6 11 6 11s6-6.5 6-11a6 6 0 0 0-6-6zm0 8.5A2.5 2.5 0 1 1 6 3.5a2.5 2.5 0 0 1 0 5z" fill="#fff"/></svg>
<p class="abs contact" style="left:556px;top:1856px">PineHollow Medical Center<br>Willow Lane Hospital<br>Campus 2240 Willow Lane,<br>Richmond Texas 77400</p>
<svg class="abs" style="left:527px;top:1988px" width="16" height="16" viewBox="0 0 24 24"><path fill="#fff" d="M6.6 10.8a15 15 0 0 0 6.6 6.6l2.2-2.2a1 1 0 0 1 1-.2 11 11 0 0 0 3.6.6 1 1 0 0 1 1 1V20a1 1 0 0 1-1 1A17 17 0 0 1 3 4a1 1 0 0 1 1-1h3.5a1 1 0 0 1 1 1c0 1.2.2 2.4.6 3.6a1 1 0 0 1-.3 1z"/></svg>
<p class="abs contact" style="left:556px;top:1982px">+1&nbsp; 281-555-0142</p>
<svg class="abs" style="left:526px;top:2041px" width="18" height="14" viewBox="0 0 18 14"><rect x="1" y="1" width="16" height="12" rx="1" stroke="#fff" stroke-width="1.6" fill="none"/><path d="M1 2l8 6 8-6" stroke="#fff" stroke-width="1.6" fill="none"/></svg>
<p class="abs contact" style="left:559px;top:2033px">info@phmc.example</p>

<div class="abs brand" style="left:830px;top:1940px;color:#fff;font-size:24px"><span class="dot" style="background:#fff;width:44px;height:44px"></span>PineHollow Medical Center</div>
<span class="abs card" style="left:830px;top:2035px;background:#f3f3f3" aria-label="Payment card"></span>
<span class="abs card" style="left:906px;top:2035px;background:#f3f3f3" aria-label="Payment card"></span>
<span class="abs card" style="left:982px;top:2035px;background:#7badd7" aria-label="Payment card"></span>
<span class="abs card" style="left:1058px;top:2035px;background:#cadeef" aria-label="Payment card"></span>

<div class="abs rule"></div>
<p class="abs copy">© copyrights 2022 PineHollowMedicalCenter |&nbsp; All Rights Reserved</p>

</body>
</html>
```